BrindleStaffing Business Card Design

We are a staffing company finding positions for dedicated nurses and physicians.

Target Market(s)

Business Professionals

Industry/Entity Type

Staffing

Contact Information for Business Card

Gregory Malden
Chairman
417 39th Crescent South
SAINT PETERSBURG FL 33719
813-555-0147 Mobile
813-555-0183 Fax
gmalden@brindlestaffing.example
www.brindlestaffing.example

Font styles to use
Sans Serif

Colors
fbee3e
f04a50
f37122

Requirements
Must have
• Logo Attached, see colors below. We'd like to see Yellow, Orange and Red.

```html
<!DOCTYPE html>
<html lang="en">
<head>
<meta charset="utf-8">
<title>BrindleStaffing Business Card</title>
<link rel="stylesheet" href="https://fonts.googleapis.com/css2?family=Open+Sans:wght@400;600;700&display=swap">
<style>
  :root {
    --backdrop: #d9d9d9;
    --card: #f7f7f7;
    --ink: #1e1e1e;
    --brand: #f04a50;
    --icon: #f37122;
    --dot-1: #f04a50;
    --dot-2: #f25d3a;
    --dot-3: #f37122;
    --dot-4: #f6952c;
    --dot-5: #f8c136;
    --dot-6: #fbee3e;
  }
  * { margin: 0; padding: 0; box-sizing: border-box; }
  html, body {
    width: 1200px; height: 864px; overflow: hidden;
    background: var(--backdrop);
    font-family: "Open Sans", sans-serif;
  }
  .canvas { position: relative; width: 1200px; height: 864px; }
  .card {
    position: absolute;
    width: 540px; height: 309px;
    background: var(--card);
    box-shadow: 0 6px 18px rgba(0,0,0,0.12);
    overflow: hidden;
  }
  .card--back { left: 600px; top: 110px; }
  .card--front { left: 60px; top: 445px; }

  .wordmark {
    position: absolute;
    font-weight: 700;
    color: var(--brand);
    letter-spacing: -0.5px;
    white-space: nowrap;
  }
  .card--back .wordmark { left: 86px; top: 104px; font-size: 46px; }
  .card--front .wordmark { left: 38px; top: 32px; font-size: 40px; }

  .holder {
    position: absolute; left: 40px; top: 102px;
    font-size: 19px; font-weight: 400; color: var(--ink);
  }
  .contact-list {
    position: absolute; left: 40px; top: 142px;
    list-style: none;
    font-size: 13px; line-height: 19px; color: var(--ink);
  }
  .contact-list li { display: flex; align-items: center; gap: 8px; white-space: nowrap; }
  .contact-list svg { width: 13px; height: 13px; flex: none; }

  .dot-column {
    position: absolute; right: 22px; top: 22px;
    width: 66px; height: 264px;
  }
</style>
</head>
<body>
<div class="canvas">

  <section class="card card--back" aria-label="Card back">
    <div class="wordmark">BrindleStaffing</div>
    <svg class="dot-column" viewBox="0 0 66 264" aria-hidden="true">
      <circle cx="50" cy="14" r="11" fill="var(--dot-1)"/>
      <circle cx="40" cy="60" r="12" fill="var(--dot-2)"/>
      <circle cx="30" cy="106" r="13" fill="var(--dot-3)"/>
      <circle cx="23" cy="153" r="14" fill="var(--dot-4)"/>
      <circle cx="21" cy="200" r="15" fill="var(--dot-5)"/>
      <circle cx="25" cy="246" r="16" fill="var(--dot-6)"/>
    </svg>
  </section>

  <section class="card card--front" aria-label="Card front">
    <div class="wordmark">BrindleStaffing</div>
    <div class="holder">Gregory Malden</div>
    <ul class="contact-list">
      <li>
        <svg viewBox="0 0 13 13"><rect width="13" height="13" rx="2" fill="var(--icon)"/><path d="M4 3l1.6 0 .6 2-1 .8a6 6 0 0 0 2.2 2.2l.8-1 2 .6V9.8A1 1 0 0 1 9 10.6 7 7 0 0 1 3 4.6 1 1 0 0 1 4 3z" fill="#fff"/></svg>
        813-555-0147
      </li>
      <li>
        <svg viewBox="0 0 13 13"><rect width="13" height="13" rx="2" fill="var(--icon)"/><rect x="2.5" y="4" width="8" height="5.5" fill="#fff"/><path d="M2.5 4l4 3 4-3" stroke="var(--icon)" stroke-width="0.9" fill="none"/></svg>
        gmalden@brindlestaffing.example
      </li>
      <li>
        <svg viewBox="0 0 13 13"><rect width="13" height="13" rx="2" fill="var(--icon)"/><circle cx="6.5" cy="6.5" r="3.8" fill="none" stroke="#fff" stroke-width="1"/><path d="M2.7 6.5h7.6M6.5 2.7c-1.8 2-1.8 5.6 0 7.6M6.5 2.7c1.8 2 1.8 5.6 0 7.6" stroke="#fff" stroke-width="0.8" fill="none"/></svg>
        www.brindlestaffing.example
      </li>
      <li>
        <svg viewBox="0 0 13 13"><rect width="13" height="13" rx="2" fill="var(--icon)"/><path d="M6.5 2.5a3 3 0 0 1 3 3c0 2.2-3 5-3 5s-3-2.8-3-5a3 3 0 0 1 3-3z" fill="#fff"/><circle cx="6.5" cy="5.5" r="1.1" fill="var(--icon)"/></svg>
        417 39th Crescent South , SAINT PETERSBURG FL 33719
      </li>
    </ul>
    <svg class="dot-column" viewBox="0 0 66 264" aria-hidden="true">
      <circle cx="50" cy="14" r="11" fill="var(--dot-1)"/>
      <circle cx="40" cy="60" r="12" fill="var(--dot-2)"/>
      <circle cx="30" cy="106" r="13" fill="var(--dot-3)"/>
      <circle cx="23" cy="153" r="14" fill="var(--dot-4)"/>
      <circle cx="21" cy="200" r="15" fill="var(--dot-5)"/>
      <circle cx="25" cy="246" r="16" fill="var(--dot-6)"/>
    </svg>
  </section>

</div>
</body>
</html>
```